Highly motivated family winery needs new wine labels.

Company and target group:
We are a smaller, family-run winery in the heart of Germany and focus on quality rather than quantity. We primarily market to private customers, but are also represented in food retail. The wines appeal to both younger and older wine drinkers (30 – 80 years old). The labels should also be accordingly.
Requirements and wishes:
We would like to have a new logo consisting of the letters L and T that can be used in both 1 color and 2 colors. The family name “Tessendorf” should appear on the label, with the font being left to the creativity of the designers. The size of the label has not yet been fixed, but it should run around the bottle and therefore have a front and back (around 160mm wide and 80mm high). The design should be simple, modern and not too ornate.
The currently 22 types of wine/sparkling wine should all have the same label, but we would like to color-code the flavors in some way.
Perhaps the silhouette of one of the buildings of our winery (with the tower) can be incorporated into the design of the label (see picture).
A central element of the labels should have a high recognition value and be placed on the front of the label with the later wine type information.
We look forward to your suggestions.
Wegen der Weihnachtsfeiertage möchte ich das Projekt verlängern, um den Designern mehr Zeit zu geben. Bisher sind auch nur wenige Worschläge eingegangen.

```html
<!DOCTYPE html>
<html lang="en">
<head>
<meta charset="utf-8">
<title>Tessendorf Rosé – Wine Label</title>
<link rel="stylesheet" href="https://fonts.googleapis.com/css2?family=Montserrat:wght@400;500&display=swap">
<style>
  :root {
    --page-bg: #ffffff;
    --label-dark: #262627;
    --label-mid: #2e2e30;
    --text-light: #e8e8e8;
    --text-soft: #d2d2d2;
    --rule: #4a4a4c;
    --accent-red: #c9373e;
  }
  html, body {
    margin: 0;
    padding: 0;
    width: 697px;
    height: 1200px;
    overflow: hidden;
    background: var(--page-bg);
    font-family: "Montserrat", sans-serif;
  }
  .label {
    position: absolute;
    left: 28px;
    top: 448px;
    width: 640px;
    height: 304px;
    background: linear-gradient(90deg, var(--label-mid) 0%, var(--label-dark) 60%, var(--label-dark) 100%);
    color: var(--text-light);
  }
  /* front panel */
  .front {
    position: absolute;
    left: 0;
    top: 0;
    width: 360px;
    height: 100%;
  }
  .front-mark {
    position: absolute;
    left: 0;
    width: 360px;
    top: 72px;
    text-align: center;
    font-weight: 500;
    font-size: 120px;
    line-height: 1;
    letter-spacing: -4px;
    color: var(--text-light);
  }
  .front-rule {
    position: absolute;
    left: 117px;
    width: 126px;
    height: 1px;
    background: var(--rule);
  }
  .front-rule.upper { top: 207px; }
  .front-rule.lower { top: 263px; }
  .family-name {
    position: absolute;
    left: 0;
    width: 360px;
    top: 224px;
    text-align: center;
    font-weight: 400;
    font-size: 20px;
    letter-spacing: 7px;
    text-indent: 7px;
    color: var(--text-light);
  }
  .wine-type {
    position: absolute;
    left: 0;
    width: 360px;
    top: 273px;
    text-align: center;
    font-weight: 400;
    font-size: 11px;
    letter-spacing: 1.5px;
    color: var(--accent-red);
  }
  /* back panel */
  .back {
    position: absolute;
    left: 385px;
    top: 0;
    width: 228px;
    height: 100%;
  }
  .back-brand {
    position: absolute;
    top: 19px;
    left: 0;
    width: 100%;
    display: flex;
    justify-content: center;
    align-items: center;
    gap: 8px;
  }
  .back-mark {
    font-weight: 500;
    font-size: 22px;
    letter-spacing: -1px;
    color: var(--text-light);
  }
  .back-divider {
    width: 1px;
    height: 20px;
    background: var(--text-soft);
  }
  .back-name {
    font-weight: 400;
    font-size: 9px;
    letter-spacing: 2.5px;
    color: var(--text-light);
  }
  .back-copy {
    position: absolute;
    top: 58px;
    left: 0;
    width: 100%;
    text-align: center;
    text-transform: uppercase;
    font-size: 6px;
    line-height: 9.7px;
    letter-spacing: 0.3px;
    color: var(--text-soft);
  }
  .back-copy p { margin: 0; }
</style>
</head>
<body>
  <section class="label" aria-label="Tessendorf rosé wine label, front and back">
    <div class="front">
      <div class="front-mark">LT</div>
      <div class="front-rule upper"></div>
      <div class="family-name">TESSENDORF</div>
      <div class="front-rule lower"></div>
      <div class="wine-type">ROSÉ</div>
    </div>
    <div class="back">
      <div class="back-brand">
        <span class="back-mark">LT</span>
        <span class="back-divider"></span>
        <span class="back-name">TESSENDORF</span>
      </div>
      <div class="back-copy">
        <p>A fresh, bright rosé from our own family vineyards in the heart of Germany. Gentle notes of wild strawberry, red currant and pink grapefruit meet a crisp, lively finish. Hand picked grapes, pressed softly and fermented cool to keep every delicate aroma of the summer harvest.</p>
        <p>Serve chilled at eight to ten degrees with light salads, grilled fish, fresh goat cheese or simply on a warm evening with friends.</p>
        <p>Grown, made and bottled by the Tessendorf family, caring for quality since generations.</p>
      </div>
    </div>
  </section>
</body>
</html>
```